Business card design for a dynamic IT consulting company

We need a business card design for a young firm, specialized in the Telecommunications/Consulting industry. The name of the company is Brask and Partners Business Consulting Ltd. (Short name: Brask and Partnes)
Brask = solve read reverse, so we aim to be uncomplicated and solution-oriented. The small pipe in our logo is also related to the word solve. So we need a new business card design, which is simple, eye catching and something non traditional (I would probably prefer a square shaped design rather than a rectangle, but open for suggestions). Attached our logo.

Target Market(s)

Usually our customers are Tier1 Telecoms providers (Q-Linkra, Parnexo, etc) and their executives.

Industry/Entity Type

Business

Contact Information for Business Card

Name: Gergely Halmindo
Email: g.halmindo@braskpartnera.hu
Web: www.braskpartnera.hu
Mobile: +36 30 555 0192
Title: Managing Director

Optional:
Company name: Brask and Partners Ltd.
Address: 1047 Budapest, Ravaszi str. 17/B, Hungary

Font styles to use
Other font styles liked:
• helveticaneue_medium, Prime Regular are used now.

Colors

Designer to choose colors to be used in the design.

Requirements
Must have
• I would like to have a 2 sided design.
Nice to have
• I thought if we make the logo a bit bigger (without the company name), that could go to the back with the company name below. I though, if the pipe in the logo is somehow touchable on the business card, would be nice and unique.

```html
<!DOCTYPE html>
<html lang="en">
<head>
<meta charset="utf-8">
<title>Brask &amp; Partners – Business Card</title>
<link href="https://fonts.googleapis.com/css2?family=Arimo:wght@400;700&display=swap" rel="stylesheet">
<style>
  :root {
    --backdrop: #c9c9c9;
    --card-white: #ffffff;
    --card-dark: #231f20;
    --magenta: #b5318f;
    --blue: #1f9ad6;
    --grey: #555555;
    --ink: #3a3a3a;
  }
  html, body {
    margin: 0;
    padding: 0;
    width: 1200px;
    height: 1008px;
    overflow: hidden;
    background: var(--backdrop);
    font-family: "Arimo", Helvetica, Arial, sans-serif;
  }
  .canvas { position: relative; width: 1200px; height: 1008px; }
  .card { position: absolute; width: 560px; height: 320px; overflow: hidden; }
  .card-front { left: 318px; top: 166px; background: var(--card-white); }
  .card-back { left: 315px; top: 527px; background: var(--card-dark); }

  .mosaic-band {
    position: absolute; left: 0; top: 0; width: 144px; height: 83px;
    background: linear-gradient(90deg, var(--magenta) 0%, var(--blue) 35%, #6b6b6b 60%, #a8d8f0 85%, rgba(255,255,255,0) 100%);
  }

  .brand-name {
    position: absolute; margin: 0;
    font-weight: 400; white-space: nowrap; line-height: 1;
  }
  .card-front .brand-name { left: 248px; top: 40px; font-size: 31px; color: var(--grey); }
  .card-front .brand-mark {
    position: absolute; left: 226px; top: 50px; width: 12px; height: 12px; background: var(--magenta);
  }
  .card-back .brand-name {
    left: 0; right: 0; top: 188px; text-align: center; font-size: 38px; color: #ffffff;
  }

  .person { position: absolute; left: 249px; top: 176px; }
  .person-name { margin: 0; font-size: 18px; font-weight: 700; color: var(--ink); }
  .person-title { margin: 3px 0 0; font-size: 14.5px; color: var(--blue); }

  .contacts { position: absolute; left: 249px; top: 232px; margin: 0; padding: 0; list-style: none; }
  .contacts li {
    display: flex; align-items: center; height: 21.5px;
    font-size: 14px; color: var(--ink);
  }
  .contacts svg { width: 15px; height: 15px; margin-right: 6px; flex: none; }
  .contacts b { font-weight: 700; }

  .address {
    position: absolute; left: 0; right: 0; top: 276px; margin: 0;
    text-align: center; font-size: 13.5px; color: #ffffff;
  }
</style>
</head>
<body>
<main class="canvas">

  <section class="card card-front" aria-label="Card front">
    <div class="mosaic-band" role="img" aria-label="Decorative square mosaic in magenta, blue and grey fading to white"></div>
    <span class="brand-mark" aria-hidden="true"></span>
    <p class="brand-name">Brask &amp; Partners</p>

    <div class="person">
      <h1 class="person-name">Gergely Halmindo</h1>
      <p class="person-title">Managing Director</p>
    </div>

    <ul class="contacts">
      <li>
        <svg viewBox="0 0 16 16" aria-hidden="true"><circle cx="8" cy="8" r="8" fill="var(--magenta)"/><path d="M4.5 7.5c0-1.6 1.6-2.5 3.5-2.5s3.5 0.9 3.5 2.5l-1.5 0v-0.8h-4v0.8zM5.5 8.5h5l0.5 2.5h-6z" fill="#fff"/></svg>
        +36 30 555 0192
      </li>
      <li>
        <svg viewBox="0 0 16 16" aria-hidden="true"><circle cx="8" cy="8" r="8" fill="var(--magenta)"/><rect x="4" y="5" width="8" height="6" fill="#fff"/><path d="M4 5l4 3.2L12 5" stroke="var(--magenta)" stroke-width="1" fill="none"/></svg>
        g.halmindo@braskpartnera.hu
      </li>
      <li>
        <svg viewBox="0 0 16 16" aria-hidden="true"><circle cx="8" cy="8" r="8" fill="var(--magenta)"/><g stroke="#fff" stroke-width="0.9" fill="none"><circle cx="8" cy="8" r="4.5"/><ellipse cx="8" cy="8" rx="2" ry="4.5"/><path d="M3.5 8h9M4.3 5.7h7.4M4.3 10.3h7.4"/></g></svg>
        <span>www.<b>braskpartnera</b>.hu</span>
      </li>
    </ul>
  </section>

  <section class="card card-back" aria-label="Card back">
    <p class="brand-name">Brask &amp; Partners</p>
    <p class="address">1047 Budapest, Ravaszi str. 17/B, Hungary</p>
  </section>

</main>
</body>
</html>
```